Kelvora Supply Export Company web

We need a web design for an existing website we have. we want it to be simple yet flashy. It's a simple 3 page informative website with a link to our email address and line card. First page would be to introduce the company. second page would be the list of items we carry and third would be the contact page. I would like SEO optimization.
I would like a black background for the Webpage with flash and SEO optimization.
Reason: Need more information need it to be SEO
It Company

```html
<!DOCTYPE html>
<html lang="en">
<head>
<meta charset="utf-8">
<title>TQS Supply – Construction Materials, Computers, Trucks</title>
<meta name="description" content="TQS Supply supplies construction materials, computers and trucks.">
<link href="https://fonts.googleapis.com/css2?family=Arimo:wght@400;700&display=swap" rel="stylesheet">
<style>
:root{
  --page-bg:#1d5068;
  --bar-top:#4a4c4e;
  --bar-bottom:#111213;
  --panel:#ffffff;
  --ink:#111111;
  --body-ink:#1e1e1e;
  --light:#ffffff;
  --nav-ink:#e4e4e4;
  --footer:#171717;
  --steel-light:#8d9094;
  --steel-dark:#2b2d30;
  --sky-light:#9fc1e6;
  --sky-dark:#3d5f8e;
  --truck-red:#c94a22;
}
*{margin:0;padding:0;box-sizing:border-box}
html,body{width:1200px;height:869px;overflow:hidden}
body{background:var(--page-bg);font-family:"Arimo",Arial,sans-serif;position:relative}
.top-bar{position:absolute;left:0;top:0;width:1200px;height:49px;background:linear-gradient(var(--bar-top),var(--bar-bottom) 60%)}
.brand{position:absolute;left:187px;top:0;width:198px;height:144px;background:linear-gradient(#ffffff 55%,#dcdcdc);z-index:3;display:flex;align-items:center;justify-content:center;gap:8px;box-shadow:0 1px 3px rgba(0,0,0,.35)}
.brand-mark{width:14px;height:14px;background:var(--page-bg)}
.brand-name{font-size:26px;font-weight:700;color:var(--ink)}
.main-nav{position:absolute;top:12px;left:0}
.main-nav a{position:absolute;text-decoration:none;font-size:17px;white-space:nowrap;color:var(--nav-ink)}
.main-nav a.active{color:var(--light)}
.phone{position:absolute;left:875px;top:10px;display:flex;align-items:center;gap:8px;color:var(--light);font-size:17px}
.phone-icon{width:27px;height:27px;background:#f2f2f2;border-radius:4px;display:flex;align-items:center;justify-content:center}
.panel{position:absolute;left:131px;top:49px;width:913px;height:751px;background:var(--panel)}
.hero{position:absolute;left:142px;top:58px;width:892px;height:432px;background:linear-gradient(160deg,#3a3c3f,#a9abae 35%,#4b4d50 60%,#1c1d1f);overflow:hidden}
.hero-caption{background:none}
.hero-title{position:absolute;left:592px;top:300px;color:var(--light);font-size:44px;line-height:43px;font-weight:400;text-shadow:0 1px 3px rgba(0,0,0,.4);white-space:nowrap}
.hero-title strong{display:block;font-weight:700}
.hero-dots{position:absolute;left:780px;top:392px;display:flex;gap:14px}
.hero-dots span{width:14px;height:14px;border-radius:50%;background:var(--light)}
.hero-dots span.ring{background:transparent;border:2.5px solid var(--light)}
.about{position:absolute;left:162px;top:519px;width:542px}
.about h1{font-size:25px;font-weight:400;color:var(--ink);margin-bottom:11px}
.about p{font-size:12.6px;line-height:23px;color:var(--body-ink);text-align:justify;letter-spacing:-.1px}
.categories{position:absolute;left:729px;top:547px;width:274px}
.category{position:absolute;left:0;width:274px;height:60px;border-radius:4px;color:var(--light);font-size:23px;display:flex;align-items:center;padding-left:22px;text-decoration:none;overflow:hidden;white-space:nowrap}
.category.materials{top:0;background:linear-gradient(var(--steel-light),var(--steel-dark));padding-left:17px}
.category.computers{top:73px;background:linear-gradient(90deg,var(--sky-light),var(--sky-dark))}
.category.trucks{top:148px;background:linear-gradient(90deg,#1c1c1c 45%,#6c6e72 70%,var(--truck-red) 85%,#8ea0b2)}
.footer{position:absolute;left:130px;top:800px;width:915px;height:42px;background:var(--footer);color:var(--light);font-size:12.6px}
.footer p{position:absolute;right:29px;top:13px}
</style>
</head>
<body>
<header class="top-bar">
  <nav class="main-nav">
    <a class="active" href="#" style="left:427px">Home</a>
    <a href="#" style="left:519px">Our Services</a>
    <a href="#" style="left:668px">Contact us</a>
  </nav>
  <div class="phone">
    <span class="phone-icon"><svg width="14" height="18" viewBox="0 0 14 18"><path d="M3 1 L6 1 L7 5 L5 6.5 C5.5 9 6.5 11 8.5 12.5 L10 11 L13 13 L12 16.5 C6 17 1 10 2 2 Z" fill="#222"/></svg></span>
    <span>( 555 ) 014-2290</span>
  </div>
</header>
<div class="brand"><span class="brand-mark"></span><span class="brand-name">TQS Supply</span></div>
<main class="panel"></main>
<section class="hero" role="img" aria-label="Stacked steel reinforcing bars"></section>
<div class="hero hero-caption">
  <h2 class="hero-title">Construction<strong>Materials</strong></h2>
  <div class="hero-dots"><span></span><span class="ring"></span><span></span></div>
</div>
<section class="about">
  <h1>About TQS Supply</h1>
  <p>Lorem Ipsum is simply dummy text of the printing and typesetting industry. Lorem Ipsum has been the industry's standard dummy text ever since the 1500s, when an unknown printer took a galley of type and scrambled it to make a type specimen book. It has survived not only five centuries, but also the leap into electronic typesetting, remaining essentially unchanged. It was popularised in the 1960s with the release of Transfex sheets containing Lorem Ipsum passages, and more recently with desktop publishing software like Folio Layout including versions of Lorem Ipsum. leap into electronic typesetting, remaining essentially unchanged. It was popularised in the 1960s with the release of Transfex sheets containing Lorem Ipsum passages, and more recently with desktop publishing software like Folio Layout including versions of Lorem Ipsum.</p>
</section>
<nav class="categories">
  <a class="category materials" href="#" role="img" aria-label="Construction materials: steel bars">Construction&nbsp;<strong>materials</strong></a>
  <a class="category computers" href="#" role="img" aria-label="Computers: office workstations">Computers</a>
  <a class="category trucks" href="#" role="img" aria-label="Trucks: red truck cab">Trucks</a>
</nav>
<footer class="footer"><p>© 2012 TQS Supply. All rights reserved.</p></footer>
</body>
</html>
```